Renata Quisby

Luxury And Style -

Black - White & Gold

Target Market(s)

Fashion

Industry/Entity Type

Fashion

Requirements
Must have
• High-End
Nice to have
• We will Print on Silk Paper

```html
<!DOCTYPE html>
<html lang="en">
<head>
<meta charset="utf-8">
<title>Renata Quisby – Letterhead</title>
<link href="https://fonts.googleapis.com/css2?family=Jost:wght@300;400&family=Roboto:wght@300;400&display=swap" rel="stylesheet">
<style>
  :root{
    --backdrop:#000226;
    --paper:#ffffff;
    --ink:#111111;
    --text-grey:#4a4a4a;
    --gold:#c9962f;
    --gold-line:#e0a732;
    --gold-pale:#ecdcb9;
    --black:#000000;
  }
  *{margin:0;padding:0;box-sizing:border-box}
  html,body{width:954px;height:1200px;overflow:hidden;background:var(--backdrop)}
  .letterhead{
    position:absolute;left:157px;top:148px;width:640px;height:905px;
    background:var(--paper);overflow:hidden;
  }
  .brand{
    position:absolute;left:64px;top:100px;width:160px;text-align:center;
  }
  .brand-name{
    font-family:'Jost',sans-serif;font-weight:300;font-size:15px;
    letter-spacing:2.6px;color:var(--ink);white-space:nowrap;
  }
  .brand-tagline{
    margin-top:4px;font-family:'Roboto',sans-serif;font-weight:300;
    font-size:8.5px;letter-spacing:.3px;color:var(--ink);
  }
  .contact{
    position:absolute;right:64px;top:82px;text-align:right;
    font-family:'Roboto',sans-serif;font-weight:400;font-size:9.5px;
    line-height:13px;color:var(--text-grey);list-style:none;
  }
  .header-rule{
    position:absolute;left:64px;top:154px;width:512px;height:1px;display:flex;
  }
  .header-rule .gold{flex:0 0 344px;background:var(--gold-line)}
  .header-rule .dark{flex:1;background:var(--black)}
  .watermark{
    position:absolute;left:0;right:0;top:468px;text-align:center;
    font-family:'Jost',sans-serif;font-weight:300;font-size:44px;
    letter-spacing:6px;color:var(--gold-pale);white-space:nowrap;
  }
  .footer-wave{position:absolute;left:0;bottom:0;width:640px;height:84px;display:block}
  .footer-wave .band-dark{fill:var(--black)}
  .footer-wave .band-gold{fill:var(--gold)}
</style>
</head>
<body>
  <main class="letterhead">
    <header>
      <div class="brand">
        <div class="brand-name">RENATA QUISBY</div>
        <div class="brand-tagline">LUXURY AND STYLE</div>
      </div>
      <ul class="contact">
        <li>+123-555-0148</li>
        <li>www.quisbyatelier.com</li>
        <li>48 Linden Row, Fairport, ST 20417</li>
      </ul>
      <div class="header-rule"><span class="gold"></span><span class="dark"></span></div>
    </header>

    <div class="watermark" aria-hidden="true">RENATA QUISBY</div>

    <svg class="footer-wave" viewBox="0 0 1149 151" preserveAspectRatio="none" aria-hidden="true">
      <path class="band-dark" d="M0 88 C150 -10 400 -20 600 30 C750 70 950 160 1149 75 L1149 151 L0 151 Z"/>
      <path class="band-gold" d="M0 100 C150 35 380 20 560 75 C640 100 680 130 723 151 L0 151 Z"/>
      <path class="band-gold" d="M1103 151 Q1130 140 1149 122 L1149 151 Z"/>
    </svg>
  </main>
</body>
</html>
```